Home Inspection Report Cover Page- House report

We complete home inspections. This is the very first cover page of our report. We are looking to redesign the front cover page for our inspection reports. The image of the home will change as the property changes. I am providing some initial thoughts for designs. But we are willing to see new and creative designs. We are the predominant company in our industry.

Here is another link to see the first page that we currently have
https://norvaleinspections.com/wp-content/uploads/2019/11/NoPoolNewHomeSample.pdf

People print these reports out so the ink level may be a consideration.

We are looking for a modern design that presents us as an authority.

8.5 x 11

Target Market(s)

Home Buyers and Real Estate Agent

Industry/Entity Type

Home Inspection

Requirements
Must have
• Brand Consistency- Our colors can be found at norvaleinspections.com or in the uploaded Trifold named NV_Trifold

Place for a photograph of the front of a home to be
Nice to have
• Color Gradients

```html
<!DOCTYPE html>
<html lang="en">
<head>
<meta charset="utf-8">
<title>Norvale Inspection Report Cover</title>
<link href="https://fonts.googleapis.com/css2?family=Signika:wght@400;600;700&display=swap" rel="stylesheet">
<style>
  :root {
    --navy: #0b4470;
    --slate: #66718f;
    --green: #8fbc55;
    --white: #ffffff;
    --backdrop: #dcdcde;
    --badge-gold: #b8a25a;
    --badge-grey: #8a8a80;
    --badge-red: #b5232f;
    --photo-sky: #5b7896;
    --photo-house: #a89a82;
  }
  * { box-sizing: border-box; margin: 0; padding: 0; }
  html, body { width: 1200px; height: 900px; overflow: hidden; }
  body {
    background: var(--backdrop);
    font-family: "Signika", sans-serif;
    position: relative;
  }
  .cover {
    position: absolute;
    left: 283px; top: 40px;
    width: 634px; height: 820px;
    background: var(--navy);
    overflow: hidden;
    box-shadow: 0 10px 30px rgba(0,0,0,0.18);
  }
  .band-top {
    position: absolute; left: 0; top: 0; width: 100%; height: 50px;
    background: var(--green);
    display: flex; align-items: center; justify-content: space-between;
    padding: 0 26px;
  }
  .cert-badge {
    width: 32px; height: 32px; border-radius: 50%;
    background: var(--badge-grey); border: 2px solid var(--navy);
  }
  .cert-badge.gold { background: var(--badge-gold); }
  .cert-badge.light { background: var(--white); }
  .brand {
    position: absolute; left: 40px; top: 74px;
    color: var(--white);
  }
  .brand-name {
    font-weight: 700; font-size: 50px; letter-spacing: 1px; line-height: 1;
    text-transform: uppercase;
  }
  .brand-tagline {
    font-weight: 700; font-size: 17px; letter-spacing: 1.5px;
    text-transform: uppercase; margin-top: 6px; padding-left: 60px;
  }
  .brand-rule {
    position: absolute; left: 40px; top: 146px; width: 300px; height: 3px;
    background: var(--white);
  }
  .discount-badge {
    position: absolute; right: 40px; top: 66px;
    width: 76px; height: 76px; border-radius: 50%;
    background: var(--badge-red); border: 4px solid var(--white);
    box-shadow: 0 0 0 3px var(--badge-red);
  }
  .slate-panel {
    position: absolute; left: 0; top: 168px; width: 520px; height: 300px;
    background: var(--slate);
  }
  .property-photo {
    position: absolute; left: 56px; top: 198px; width: 530px; height: 250px;
    background: linear-gradient(180deg, var(--photo-sky) 0%, #7e8ea0 40%, var(--photo-house) 75%, #8c7d66 100%);
  }
  .monogram-ring {
    position: absolute; left: 0; top: 468px;
  }
  .report-details {
    position: absolute; left: 330px; top: 490px; width: 270px;
    color: var(--white); font-size: 16px; line-height: 1.55;
  }
  .detail-group {
    display: flex; gap: 12px; padding-bottom: 14px; margin-bottom: 16px;
    border-bottom: 1.5px solid var(--green);
  }
  .detail-group:last-child { border-bottom: none; }
  .detail-icon { flex: 0 0 20px; padding-top: 3px; }
  .detail-text strong { font-weight: 600; }
  .band-bottom {
    position: absolute; left: 0; bottom: 0; width: 100%; height: 58px;
    background: var(--green);
    display: flex; align-items: center; justify-content: space-between;
    padding: 0 28px;
    color: var(--white); font-weight: 600; font-size: 26px;
  }
  .phone { display: flex; align-items: center; gap: 10px; }
</style>
</head>
<body>
  <main class="cover">
    <header class="band-top">
      <div class="cert-badge light"></div>
      <div class="cert-badge gold"></div>
      <div class="cert-badge"></div>
      <div class="cert-badge"></div>
    </header>

    <div class="brand">
      <div class="brand-name">Norvale</div>
      <div class="brand-tagline">Inspection Professionals</div>
    </div>
    <div class="brand-rule"></div>
    <div class="discount-badge"></div>

    <div class="slate-panel"></div>
    <div class="property-photo" role="img" aria-label="Photograph of the front of the inspected home"></div>

    <svg class="monogram-ring" width="330" height="300" viewBox="0 0 330 300" aria-hidden="true">
      <circle cx="150" cy="170" r="150" fill="none" stroke="var(--slate)" stroke-width="28"/>
    </svg>

    <section class="report-details">
      <div class="detail-group">
        <svg class="detail-icon" width="20" height="22" viewBox="0 0 20 22" aria-hidden="true">
          <circle cx="11" cy="8" r="6" fill="none" stroke="var(--green)" stroke-width="3"/>
          <line x1="7" y1="12.5" x2="2" y2="19" stroke="var(--green)" stroke-width="3.5" stroke-linecap="round"/>
        </svg>
        <div class="detail-text">
          For Mark &amp; Ellen Carter<br>
          By <strong>Dana Reyes (#12345)</strong><br>
          Date 3/1/2020
        </div>
      </div>
      <div class="detail-group">
        <svg class="detail-icon" width="20" height="24" viewBox="0 0 20 24" aria-hidden="true">
          <path d="M10 1a8 8 0 0 0-8 8c0 6 8 14 8 14s8-8 8-14a8 8 0 0 0-8-8z" fill="var(--green)"/>
          <circle cx="10" cy="9" r="3" fill="var(--navy)"/>
        </svg>
        <div class="detail-text">
          1234 Main Street<br>
          Client Town<br>
          CT
        </div>
      </div>
    </section>

    <footer class="band-bottom">
      <div class="phone">
        <svg width="20" height="26" viewBox="0 0 20 26" aria-hidden="true">
          <path d="M6 2 L10 2 L10 8 L7 9 Q7 13 7 17 L10 18 L10 24 L6 24 Q1 20 1 13 Q1 6 6 2 Z" fill="var(--white)"/>
        </svg>
        <span>800-555-0142</span>
      </div>
      <span class="website">norvaleinspections.com</span>
    </footer>
  </main>
</body>
</html>
```